Business Card Design

We are a flooring/granite/cabinet company
want a sleek and modern design card. Will send our logo. maybe our logo in 3d on card.
black card

Industry/Entity Type

Business

Contact Information for Business Card

Gregory Tallis
company name Stone Hearth Depot
4827 fm 71s 78540
210-634-8872
stonehearthdepot@mailvista.example

```html
<!DOCTYPE html>
<html lang="en">
<head>
<meta charset="utf-8">
<title>Stone Hearth Depot — Business Card</title>
<link href="https://fonts.googleapis.com/css2?family=Roboto:wght@400;700&display=swap" rel="stylesheet">
<style>
  :root {
    --backdrop: #a4a4a4;
    --card: #1d1d1d;
    --text: #c9c9c9;
    --text-strong: #e2e2e2;
    --accent: #2f9a2f;
    --rule: #2c7a2c;
  }
  * { box-sizing: border-box; margin: 0; padding: 0; }
  html, body {
    width: 1200px; height: 900px; overflow: hidden;
    background: var(--backdrop);
    font-family: "Roboto", Arial, sans-serif;
  }
  .sheet {
    width: 1200px; height: 900px;
    display: flex; flex-direction: column;
    align-items: center; justify-content: center; gap: 60px;
  }
  .card {
    position: relative;
    width: 560px; height: 320px;
    background: var(--card);
    box-shadow: 0 6px 18px rgba(0,0,0,0.25);
    color: var(--text);
  }
  .card__rule {
    position: absolute; height: 1px; background: var(--rule);
  }

  /* Front face */
  .card--front .card__rule { left: 64px; right: 28px; top: 168px; }
  .brand {
    position: absolute; left: 0; right: 0; top: 104px;
    display: flex; align-items: center; justify-content: center; gap: 12px;
  }
  .brand__mark { width: 18px; height: 18px; background: var(--accent); }
  .brand__name {
    font-size: 27px; font-weight: 700; letter-spacing: 1px;
    text-transform: uppercase; color: var(--text-strong);
  }
  .card--front .address {
    position: absolute; left: 0; right: 0; top: 190px;
    text-align: center; font-size: 13px; line-height: 18px;
  }

  /* Contact face */
  .card--contact .card__rule { left: 40px; right: 40px; top: 212px; }
  .contact {
    position: absolute; left: 40px; top: 70px;
    font-size: 13px; line-height: 18px;
  }
  .contact__name { font-weight: 700; font-size: 15px; color: var(--text-strong); }
  .contact__role { text-transform: uppercase; }
  .card--contact .brand {
    left: auto; right: 56px; top: 150px;
  }
  .card--contact .brand__mark { width: 40px; height: 40px; }
  .card--contact .address {
    position: absolute; right: 40px; top: 232px;
    text-align: right; font-size: 13px; line-height: 18px;
  }
</style>
</head>
<body>
  <main class="sheet">
    <section class="card card--front" aria-label="Card front">
      <div class="brand">
        <span class="brand__mark"></span>
        <span class="brand__name">Stone Hearth Depot</span>
      </div>
      <div class="card__rule"></div>
      <p class="address">Stone Hearth Depot<br>4827 fm 71s 78540</p>
    </section>

    <section class="card card--contact" aria-label="Card back">
      <div class="contact">
        <p class="contact__name">Gregory Tallis</p>
        <p class="contact__role">Founder &amp; CEO</p>
        <p class="contact__email">stonehearthdepot@mailvista.example</p>
        <p class="contact__phone">210-634-8872</p>
      </div>
      <div class="brand">
        <span class="brand__mark"></span>
      </div>
      <div class="card__rule"></div>
      <p class="address">Stone Hearth Depot<br>4827 fm 71s 78540</p>
    </section>
  </main>
</body>
</html>
```